One Page Sales Flyer for Wireless Survey- Computer Hardware

I want a designer to create a one page 4 color sales slick to be given to our sales team to sell to the end customers. I would like a visual picture of a heat map so zavvix "heat map wireless" to get an idea of how that image should look.

```html
<!DOCTYPE html>
<html lang="en">
<head>
<meta charset="utf-8">
<title>Brelvony – Wireless Site Surveys Flyer</title>
<link rel="stylesheet" href="https://fonts.googleapis.com/css2?family=Nunito+Sans:wght@400;600;700;800&family=Montserrat:wght@500&display=swap">
<style>
  :root {
    --blue: #3a8fd1;
    --ink: #3a3a3a;
    --heading: #222222;
    --dark: #333436;
    --paper: #ffffff;
    --backdrop: #e9eaec;
  }
  * { box-sizing: border-box; margin: 0; padding: 0; }
  html, body { width: 1200px; height: 800px; overflow: hidden; }
  body {
    background: var(--backdrop);
    font-family: "Nunito Sans", Arial, sans-serif;
    color: var(--ink);
    position: relative;
  }
  .flyer {
    position: absolute; left: 290px; top: 15px;
    width: 620px; height: 770px;
    background: var(--paper);
    box-shadow: 0 4px 18px rgba(0,0,0,.18);
    overflow: hidden;
  }
  .hero-photo {
    position: absolute; left: 0; top: 0; width: 620px; height: 197px;
    background: linear-gradient(180deg, #e4e6e9 0%, #a9adb3 45%, #5d6168 100%);
  }
  .brand {
    position: absolute; right: 24px; top: 14px;
    display: flex; flex-direction: column; align-items: center; gap: 6px;
  }
  .brand-square { width: 40px; height: 40px; background: var(--blue); }
  .brand-name {
    font-family: "Montserrat", sans-serif; font-weight: 500;
    font-size: 21px; letter-spacing: 1px; color: var(--heading);
  }
  .info-column {
    position: absolute; left: 54px; top: 229px; width: 232px;
    font-size: 9.6px; line-height: 11.6px; text-align: justify;
  }
  .info-column h2 { font-size: 10.2px; line-height: 12px; font-weight: 800; color: var(--heading); }
  .info-column p { margin-bottom: 13px; }
  .info-column ol { padding-left: 15px; }
  .info-column li { margin-bottom: 1px; }
  .headline {
    position: absolute; left: 315px; top: 225px;
    font-size: 15.5px; font-weight: 800; color: var(--blue); line-height: 1.13;
  }
  .headline .with { font-weight: 400; color: var(--heading); }
  .headline .big { font-size: 17.5px; }
  .customers {
    position: absolute; left: 315px; top: 312px; width: 260px; height: 277px;
    background: var(--blue);
  }
  .customers h3 {
    background: var(--dark); color: #fff;
    font-size: 14px; font-weight: 800; padding: 7px 15px; height: 31px;
  }
  .customers ul { list-style: none; padding: 12px 16px; color: #fff; font-size: 16px; line-height: 22px; }
  .footnote { position: absolute; left: 315px; top: 618px; font-size: 8.5px; line-height: 1.3; }
  .contact-band {
    position: absolute; left: 0; bottom: 0; width: 620px; height: 83px;
    background: var(--dark); color: #fff; text-align: center; padding-top: 14px;
  }
  .contact-band .web { font-size: 16px; font-weight: 800; }
  .contact-band .lines { font-size: 16px; margin-top: 2px; }
</style>
</head>
<body>
  <article class="flyer">
    <div class="hero-photo" role="img" aria-label="Photo of four colleagues meeting at a table with laptops in a bright office"></div>
    <div class="brand">
      <span class="brand-square"></span>
      <span class="brand-name">BRELVONY</span>
    </div>

    <section class="info-column">
      <h2>What is a wireless site survey or heat map?</h2>
      <p>A wireless site survey is a compilation of reports showing a visual representation of health of your wireless network. This does not only show how strong or weak a wireless signal is in any location it also helps aid in channel and placement to ensure maximum stable data rates are archived even where the single appears strong.</p>
      <h2>Why do customers need a site survey?</h2>
      <p>Any variety of factors can contribute to an unhealthy wireless network (electrical, motors, materials used in construction, distance, neighboring wireless networks, etc.) and traditional methods that use only blueprints and a computer program to show signal strength have shown to be ineffective.</p>
      <h2>Why should they use you?</h2>
      <ol>
        <li>42% of businesses report some issues with wireless connectivity and acknowledge its effect on the bottom line*</li>
        <li>Most of these problems are solved through either fine tuning the current equipment (managed services) or purchasing new equipment (incremental sales) of which you can provide both</li>
        <li>Being a one-stop shop for all your customer's IT needs prevents them from needing additional vendors</li>
        <li>The increase of IoT (Internet of things) and BYOD (Bring Your Own Device)</li>
      </ol>
    </section>

    <h1 class="headline">Increase Hardware<br>and Services Spend<br><span class="with">with</span> <span class="big">Wireless Site Surveys</span></h1>

    <section class="customers">
      <h3>TARGET CUSTOMERS</h3>
      <ul>
        <li>Distributors</li>
        <li>Warehouses</li>
        <li>SLED</li>
        <li>K-12</li>
        <li>Medical / Hospitals</li>
        <li>Enterprise F1000</li>
        <li>Sports Venues</li>
        <li>Stadiums</li>
        <li>Hotels</li>
        <li>Retail stores</li>
      </ul>
    </section>

    <p class="footnote">* Newswire Daily. "Connectivity in the Modern Enterprise".<br>June 2017</p>

    <footer class="contact-band">
      <div class="web">www.yourbrelvony.com</div>
      <div class="lines">info@yourbrelvony.com &nbsp;|&nbsp; 555-014-2368</div>
    </footer>
  </article>
</body>
</html>
```